Roofing & Siding door hanger flyer

-Looking to make door hanger flyer for Pellmont Roofing & Siding
-4.5" wide x 11" tall
-2 sided full colour
-We have started a new website (the content is changing) I have attached photos.
-About us:
-25 year labour warranty's available
-32 years in Calgary
-QCR A+ Member
-NWTG (Prairie Joint Shingle Guild) (logo attached)
-KOV Summit Select (logo attached)
-Owen Brisket (logo attached)
-Slogan "Raised On Care, Proven Through Seasons" 32 years in Calgary
-Sale
-Page 1 & 2 design ideas
We are in your area, contact us today for your Exclusive limited time offer! *discounts apply exclusively to new agreements only
Updates
-Please keep simple, clean & bright
-I really like the bright blue from our new logo (new logo uploaded)
-We specialize in Roofing -Siding-Gutters & full Exterior Renos (like the competitor example uploaded)
-This is the NEW website we are currently working on (not finished) https://mockview.example-draftpad.net/view/1a2b3c4d-5e6f-4a7b-8c9d-0e1f2a3b4c5d-7k2m/?fullscreen
-This is our OLD website https://pellmontshingleworks.com
-For the sale "We are in your area, contact us today for your Exclusive limited time offer" *discounts apply exclusively to new agreements only
-Free Estimates
-our phone# is 403-555-0148
-our website is pellmontshingleworks.com
-keep simple, clean, bright use the "new logo" uploaded. Check out the competitor example uploaded file
-We are in your area, Contact us today for your Exclusive limited time offer! *discounts apply to new agreements only
-FREE ESTIMATES
-Specialized in Roofing /Siding /Gutters Full Exterior Reno's
-We are currently working on a NEW website https://mockview.example-draftpad.net/view/1a2b3c4d-5e6f-4a7b-8c9d-0e1f2a3b4c5d-7k2m/?fullscreen
-Our OLD website https://pellmontshingleworks.com/
-Post old site address on flyer pellmontshingleworks.com
-Phone # 403-555-0148
Target Market(s)
40-55
Industry/Entity Type
Roofing Siding & full Exterior Reno's
Look and feel

```html
<!DOCTYPE html>
<html lang="en">
<head>
<meta charset="utf-8">
<title>Pellmont Roofing &amp; Siding – Door Hanger</title>
<link href="https://fonts.googleapis.com/css2?family=Montserrat:wght@500;600;700;800;900&display=swap" rel="stylesheet">
<style>
:root{
  --page:#e8e9eb;
  --blue:#1a7de0;
  --blue-deep:#0e5fb8;
  --red:#e3161b;
  --ink:#1b1b1b;
  --sky:#dcebfb;
  --white:#ffffff;
}
*{box-sizing:border-box;margin:0;padding:0}
html,body{width:1200px;height:2257px;overflow:hidden;background:var(--page)}
body{position:relative;font-family:"Montserrat",sans-serif;color:var(--ink)}
.hanger{position:absolute;width:385px;height:942px;overflow:hidden;background:var(--white)}
.hanger--front{left:145px;background:linear-gradient(180deg,var(--sky) 0%,#e9f2fc 45%,var(--white) 100%)}
.hanger--back{left:643px;background:linear-gradient(160deg,#e4eefb 0%,#f6f9fe 40%,var(--white) 70%)}
.row-top{top:83px}
.row-bottom{top:1193px}
.abs{position:absolute;white-space:nowrap;line-height:1}
.center{left:0;right:0;text-align:center}

.neighbourhood{top:10px;font-weight:800;color:var(--blue-deep);font-size:13px}
.neighbourhood b{font-size:20px;font-weight:800}

.brand{top:200px;font-weight:800;color:var(--blue-deep)}
.brand .name{font-size:44px;letter-spacing:1px;display:block}
.brand .sub{font-size:17px;letter-spacing:4px;display:block;margin-top:8px}
.brand .mark{display:inline-block;width:14px;height:14px;background:var(--blue);margin-right:8px;vertical-align:3px}

.photo-house{left:0;right:0;top:300px;height:240px;position:absolute;
  background:linear-gradient(180deg,rgba(220,235,251,0) 0%,#b9c6d2 25%,#8e9aa3 55%,#c9d1d6 85%,rgba(255,255,255,.2) 100%)}
.photo-roof{left:0;right:0;top:570px;height:225px;position:absolute;
  background:linear-gradient(180deg,#dde5ee 0%,#8d8a8c 35%,#6f6b6c 65%,rgba(255,255,255,.9) 100%)}

.outlined{paint-order:stroke fill;-webkit-text-stroke:5px var(--white);font-weight:900}
.title-roofing{top:460px;font-size:54px;color:var(--blue)}
.roof-types{top:526px;font-size:25px;font-weight:700;color:var(--blue-deep)}
.title-siding{top:590px;font-size:54px;color:var(--blue-deep)}
.siding-item{font-size:17px;font-weight:700;color:var(--blue);paint-order:stroke fill;-webkit-text-stroke:4px var(--white)}
.title-ext{top:760px;font-size:35px;color:var(--red)}
.ext-item{font-size:14px;font-weight:500}

.footer{position:absolute;left:0;right:0;bottom:0;height:51px;background:var(--blue-deep);color:var(--white);text-align:center;border-top:3px solid var(--white);box-shadow:0 -2px 0 var(--blue)}
.footer .phone{display:block;font-size:21px;font-weight:600;margin-top:6px;line-height:1}
.footer .web{display:block;font-size:11.5px;font-weight:600;letter-spacing:.6px;margin-top:4px;line-height:1}

.slogan{top:180px;font-size:25px;font-weight:800;color:var(--blue);line-height:1.4;letter-spacing:-.2px}
.years{top:273px;font-size:27px;font-weight:800;color:var(--red)}
.copy{left:25px;font-size:14px;font-weight:600;line-height:1.25;white-space:normal;width:340px}
.free{top:430px;left:25px;font-size:27px;font-weight:800;color:var(--blue)}
.special{top:500px;left:25px;font-size:21px;font-weight:800;color:var(--red);text-decoration:underline;text-underline-offset:3px}
.spec-item{font-size:19px;font-weight:700;color:var(--blue-deep)}
.photo-crew{position:absolute;left:0;right:0;top:590px;height:225px;
  background:linear-gradient(100deg,#8a9a5a 0%,#2f6fc4 25%,#9aa3a8 55%,#3c3f44 80%,#d9dde0 100%)}
.badges{position:absolute;left:0;right:0;top:815px;height:73px;display:flex;align-items:center;justify-content:space-around;padding:0 10px}
.badge{display:block}
.badge--circle{width:36px;height:36px;border-radius:50%;background:#b08d2a}
.badge--wide{width:72px;height:26px;background:#1d4e8a;border-radius:3px}
.badge--square{width:30px;height:30px;background:var(--red)}
.badge--diamond{width:28px;height:28px;background:#1b3f8b;transform:rotate(45deg)}
.badge--small{width:38px;height:24px;background:#8fa2bd}
.badge--dot{width:52px;height:14px;background:#3a7d3a;border-radius:7px}

.cutout{position:absolute;left:0;top:0;width:385px;height:200px}
</style>
</head>
<body>

<section class="hanger hanger--front row-top">
  <p class="abs center neighbourhood">WE'RE IN YOUR <b>NEIGHBOURHOOD!</b></p>
  <div class="photo-house" role="img" aria-label="Photo of a large two-storey home with a new roof"></div>
  <div class="photo-roof" role="img" aria-label="Photo of a shingled roof gable with siding"></div>
  <p class="abs center brand"><span class="name"><span class="mark"></span>Pellmont</span><span class="sub">ROOFING &amp; SIDING</span></p>
  <p class="abs center outlined title-roofing">ROOFING</p>
  <p class="abs center roof-types">• Asphalt &nbsp;• Rubber &nbsp;• Metal</p>
  <p class="abs center outlined title-siding">SIDING</p>
  <p class="abs siding-item" style="left:10px;top:658px">• Brisket fibre cement</p>
  <p class="abs siding-item" style="left:267px;top:658px">• Vinyl</p>
  <p class="abs siding-item" style="left:10px;top:694px">• Metal(steel, Aluminum)</p>
  <p class="abs siding-item" style="left:267px;top:694px">• Longboard</p>
  <p class="abs center outlined title-ext">FULL EXTERIORS</p>
  <p class="abs ext-item" style="left:26px;top:804px">• Eavestrough /soffit/ Fascia</p>
  <p class="abs ext-item" style="left:26px;top:826px">• Stone</p>
  <p class="abs ext-item" style="left:26px;top:847px">• Insulation Windows &amp; Doors</p>
  <p class="abs ext-item" style="left:26px;top:869px">• Shake Repairs</p>
  <p class="abs ext-item" style="left:283px;top:804px">• Stucco</p>
  <p class="abs ext-item" style="left:283px;top:826px">• Skylights</p>
  <p class="abs ext-item" style="left:283px;top:847px">• Painting</p>
  <div class="footer"><span class="phone">(403) 555-0148</span><span class="web">www.pellmontshingleworks.com</span></div>
</section>

<section class="hanger hanger--back row-top">
  <p class="abs center slogan">Raised On Care,<br>Proven Through Seasons</p>
  <p class="abs center years">32 YEARS IN CALGARY</p>
  <p class="abs copy" style="top:316px">We are in your area, contact us today for your Exclusive limited time offer</p>
  <p class="abs copy" style="top:368px">*Discounts apply exclusively to new agreements only</p>
  <p class="abs free">FREE ESTIMATES</p>
  <p class="abs special">SPECIALIZED IN</p>
  <p class="abs spec-item" style="left:36px;top:530px">• Roofing</p>
  <p class="abs spec-item" style="left:235px;top:530px">• Siding</p>
  <p class="abs spec-item" style="left:36px;top:558px">• Gutters Full Exterior Reno's</p>
  <div class="photo-crew" role="img" aria-label="Photo of a roofer on a ladder cleaning a gutter"></div>
  <div class="badges">
    <span class="badge badge--small"></span><span class="badge badge--wide"></span><span class="badge badge--square"></span><span class="badge badge--circle"></span><span class="badge badge--diamond"></span><span class="badge badge--dot"></span>
  </div>
  <div class="footer"><span class="phone">(403) 555-0148</span><span class="web">www.pellmontshingleworks.com</span></div>
</section>

<section class="hanger hanger--front row-bottom">
  <p class="abs center neighbourhood">WE'RE IN YOUR <b>NEIGHBOURHOOD!</b></p>
  <div class="photo-house" role="img" aria-label="Photo of a large two-storey home with a new roof"></div>
  <div class="photo-roof" role="img" aria-label="Photo of a shingled roof gable with siding"></div>
  <p class="abs center brand"><span class="name"><span class="mark"></span>Pellmont</span><span class="sub">ROOFING &amp; SIDING</span></p>
  <p class="abs center outlined title-roofing">ROOFING</p>
  <p class="abs center roof-types">• Asphalt &nbsp;• Rubber &nbsp;• Metal</p>
  <p class="abs center outlined title-siding">SIDING</p>
  <p class="abs siding-item" style="left:10px;top:658px">• Brisket fibre cement</p>
  <p class="abs siding-item" style="left:267px;top:658px">• Vinyl</p>
  <p class="abs siding-item" style="left:10px;top:694px">• Metal(steel, Aluminum)</p>
  <p class="abs siding-item" style="left:267px;top:694px">• Longboard</p>
  <p class="abs center outlined title-ext">FULL EXTERIORS</p>
  <p class="abs ext-item" style="left:26px;top:804px">• Eavestrough /soffit/ Fascia</p>
  <p class="abs ext-item" style="left:26px;top:826px">• Stone</p>
  <p class="abs ext-item" style="left:26px;top:847px">• Insulation Windows &amp; Doors</p>
  <p class="abs ext-item" style="left:26px;top:869px">• Shake Repairs</p>
  <p class="abs ext-item" style="left:283px;top:804px">• Stucco</p>
  <p class="abs ext-item" style="left:283px;top:826px">• Skylights</p>
  <p class="abs ext-item" style="left:283px;top:847px">• Painting</p>
  <svg class="cutout" viewBox="0 0 385 200" aria-hidden="true">
    <rect x="0" y="72" width="190" height="54" rx="27" fill="var(--page)"/>
    <rect x="0" y="72" width="60" height="54" fill="var(--page)"/>
    <circle cx="188" cy="99" r="75" fill="var(--page)"/>
  </svg>
  <div class="footer"><span class="phone">(403) 555-0148</span><span class="web">www.pellmontshingleworks.com</span></div>
</section>

<section class="hanger hanger--back row-bottom">
  <p class="abs center slogan">Raised On Care,<br>Proven Through Seasons</p>
  <p class="abs center years">32 YEARS IN CALGARY</p>
  <p class="abs copy" style="top:316px">We are in your area, contact us today for your Exclusive limited time offer</p>
  <p class="abs copy" style="top:368px">*Discounts apply exclusively to new agreements only</p>
  <p class="abs free">FREE ESTIMATES</p>
  <p class="abs special">SPECIALIZED IN</p>
  <p class="abs spec-item" style="left:36px;top:530px">• Roofing</p>
  <p class="abs spec-item" style="left:235px;top:530px">• Siding</p>
  <p class="abs spec-item" style="left:36px;top:558px">• Gutters Full Exterior Reno's</p>
  <div class="photo-crew" role="img" aria-label="Photo of a roofer on a ladder cleaning a gutter"></div>
  <div class="badges">
    <span class="badge badge--small"></span><span class="badge badge--wide"></span><span class="badge badge--square"></span><span class="badge badge--circle"></span><span class="badge badge--diamond"></span><span class="badge badge--dot"></span>
  </div>
  <svg class="cutout" viewBox="0 0 385 200" aria-hidden="true">
    <rect x="0" y="72" width="190" height="54" rx="27" fill="var(--page)"/>
    <rect x="0" y="72" width="60" height="54" fill="var(--page)"/>
    <circle cx="188" cy="99" r="75" fill="var(--page)"/>
  </svg>
  <div class="footer"><span class="phone">(403) 555-0148</span><span class="web">www.pellmontshingleworks.com</span></div>
</section>

</body>
</html>
```